Unique, Impressive, and Modern Business Card

Looking for a distinctive, unique business card. We are distributors of tire repairs supplies, tools, machinery, and chemicals. Our target market are tire repair shops, tire franchises, and mechanic shops. We would like our design to include tire characteristics, and use our business colors. Feel free to use all types design and printing options (emboss, spot uv, foil, etc) QR code may be applied, you can use different size business cards ( standard, square, rounded edge, colored edge, etc), all formats needed for printing, also editable for future changes

Target Market(s)

Automotive, Tire industries

Industry/Entity Type

Tire Industry (automotive)

Contact Information for Business Card

Business logo, business Name (Corvane Supply Inc), Name (Marcus Pellow), Position (President) Address (58 Fernhollow Lane, Brentwood NY 11742), Contact number (Company 1-855-302-4418, Cell 1-631-245-9073, email address (marcus.pellow@corvanesupply.com), URL (www.corvanesupply.com

Requirements
Must have
• Must include Business Colors (Black, Green, Blue, White) see sample website file
Nice to have
• emboss, spot uv, etc

```html
<!DOCTYPE html>
<html lang="en">
<head>
<meta charset="utf-8">
<title>Corvane Supply Inc – Business Card</title>
<link rel="stylesheet" href="https://fonts.googleapis.com/css2?family=Arimo:wght@400;700&display=swap">
<style>
  :root {
    --stage: #2b2b30;
    --card-black: #161616;
    --card-white: #ffffff;
    --ink: #111111;
    --accent-blue: #3d4fb0;
    --accent-green: #2e9e4f;
    --emboss-light: #8a8a8a;
  }
  * { margin: 0; padding: 0; box-sizing: border-box; }
  html, body {
    width: 1200px; height: 800px; overflow: hidden;
    background: var(--stage);
    font-family: "Arimo", Arial, sans-serif;
  }
  .canvas {
    position: relative; width: 1200px; height: 800px;
    display: flex; flex-direction: column; align-items: center; justify-content: center; gap: 36px;
  }
  .card {
    position: relative; width: 620px; height: 354px;
    border-radius: 28px; overflow: hidden;
    box-shadow: 0 14px 34px rgba(0,0,0,.45);
  }
  /* Front */
  .card-front {
    background: var(--card-black);
    display: flex; align-items: center; justify-content: center; gap: 16px;
  }
  .card-front .brand-dot {
    width: 32px; height: 32px; border-radius: 50%;
    background: var(--accent-green);
  }
  .card-front .brand-name {
    font-size: 40px; font-weight: 700; letter-spacing: 1px; white-space: nowrap;
    color: var(--emboss-light); text-transform: uppercase;
  }
  /* Back */
  .card-back {
    background: var(--card-white);
    display: grid; grid-template-columns: 300px 1px 1fr; align-items: center;
  }
  .brand-block {
    display: flex; align-items: center; justify-content: center; gap: 10px;
    height: 100%; padding: 0 20px;
  }
  .brand-block .brand-dot {
    width: 22px; height: 22px; border-radius: 50%; background: var(--accent-blue); flex: none;
  }
  .brand-block .brand-name {
    font-size: 25px; font-weight: 700; color: var(--ink); text-transform: uppercase;
    letter-spacing: .5px; white-space: nowrap;
  }
  .divider { width: 1px; height: 210px; background: var(--accent-blue); }
  .contact-block { padding-left: 30px; padding-right: 16px; color: var(--ink); }
  .person-name { font-size: 25px; font-weight: 400; text-transform: uppercase; line-height: 1.05; white-space: nowrap; }
  .person-title { font-size: 17px; color: var(--accent-blue); text-transform: uppercase; margin-bottom: 18px; }
  .address { font-size: 15px; line-height: 1.3; margin-bottom: 16px; }
  .contact-list { list-style: none; font-size: 15px; line-height: 1.5; }
  .contact-list li { display: flex; align-items: center; gap: 9px; white-space: nowrap; }
  .contact-list svg { width: 13px; height: 13px; flex: none; }
</style>
</head>
<body>
<main class="canvas">
  <section class="card card-front" aria-label="Card front">
    <span class="brand-dot" aria-hidden="true"></span>
    <span class="brand-name">Corvane Supply</span>
  </section>

  <section class="card card-back" aria-label="Card back">
    <div class="brand-block">
      <span class="brand-dot" aria-hidden="true"></span>
      <span class="brand-name">Corvane Supply</span>
    </div>
    <div class="divider" aria-hidden="true"></div>
    <div class="contact-block">
      <p class="person-name">Marcus Pellow</p>
      <p class="person-title">President</p>
      <p class="address">58 Fernhollow Lane<br>Brentwood NY 11742</p>
      <ul class="contact-list">
        <li>
          <svg viewBox="0 0 16 16" aria-hidden="true"><path d="M4 1 L6.5 4.5 L5 6.5 Q7 10 9.5 11 L11.5 9.5 L15 12 L13 15 Q5 14 1 3 Z" fill="var(--accent-blue)"/></svg>
          1-855-302-4418
        </li>
        <li>
          <svg viewBox="0 0 16 16" aria-hidden="true"><rect x="4" y="1" width="8" height="14" rx="1.5" fill="none" stroke="var(--accent-blue)" stroke-width="1.6"/><circle cx="8" cy="12.5" r="0.9" fill="var(--accent-blue)"/></svg>
          1-631-245-9073
        </li>
        <li>
          <svg viewBox="0 0 16 16" aria-hidden="true"><rect x="1" y="3" width="14" height="10" fill="var(--accent-blue)"/><path d="M1 3 L8 9 L15 3" fill="none" stroke="#fff" stroke-width="1.2"/></svg>
          marcus.pellow@corvanesupply.com
        </li>
        <li>
          <svg viewBox="0 0 16 16" aria-hidden="true"><circle cx="8" cy="8" r="6.5" fill="none" stroke="var(--accent-blue)" stroke-width="1.4"/><ellipse cx="8" cy="8" rx="2.8" ry="6.5" fill="none" stroke="var(--accent-blue)" stroke-width="1.1"/><path d="M1.5 8 H14.5" stroke="var(--accent-blue)" stroke-width="1.1"/></svg>
          www.corvanesupply.com
        </li>
      </ul>
    </div>
  </section>
</main>
</body>
</html>
```